Health and Wellness Company Business Card

I need a business card design that is clean and uses modern minimalist style. The design should incorporate our logo (see attached). I would also like to use embossing on the cards so that they also have a great feel. I am open to the card using one or more colors, and these do not have to correspond to the colors in the concept paper. The card can either be one-sided or use both sides of the card.The logo uses the Avenir font.

I will need the file designed in Adobe CS and compatible with CS5.5 (Illustrator preferable) and I'll need the working file (for example: .ai) once the project is complete so that I can change the names/contact info/etc for each variation of the card.

This needs to be a memorable card for the recipient. They should think: "This is a great business card" either because of its simplicity or embossing effects or use of color.

Target Market(s)

The audience for our company has two main groups: people who pay for healthcare (insurers, companies, researcher companies) and people with chronic health conditions who are the consumers of our services and resources.

Industry/Entity Type

Business

Requirements
Must have
• Essential components of the card include: Company logo, contact Name (Mark Tolley), phone number (5808127346), email address (mtolley@brenquora.com), slogan/tagline that consists of ~30-40 characters (Use Lorem Ipsum)
Nice to have
• These fall just slightly short of "must have" to allow for design flexibility: Embossing or spot varnish effects and a splash of color
Should not have
• Designs with these components will not be successful: flashy or showy designs that are not professional in appearance, and lots of different colors

```html
<!DOCTYPE html>
<html lang="en">
<head>
<meta charset="utf-8">
<title>Brenquora Business Card</title>
<link rel="stylesheet" href="https://fonts.googleapis.com/css2?family=Montserrat:wght@400;500&display=swap">
<style>
  :root {
    --page-bg: #5a5a5a;
    --card-bg: #0f0f0f;
    --ink: #8a8a8e;
    --ink-soft: #7a7a7e;
  }
  html, body {
    margin: 0;
    padding: 0;
    width: 1200px;
    height: 900px;
    overflow: hidden;
    background: var(--page-bg);
  }
  .canvas {
    position: relative;
    width: 1200px;
    height: 900px;
    display: flex;
    align-items: center;
    justify-content: center;
  }
  .business-card {
    position: relative;
    width: 1050px;
    height: 600px;
    background: var(--card-bg);
    border-radius: 6px;
    font-family: "Montserrat", "Helvetica Neue", Arial, sans-serif;
    color: var(--ink);
  }
  .brand {
    position: absolute;
    top: 70px;
    left: 0;
    right: 0;
    display: flex;
    flex-direction: column;
    align-items: center;
  }
  .brand-mark {
    width: 110px;
    height: 110px;
    border-radius: 50%;
    background: var(--ink);
  }
  .brand-name {
    margin-top: 34px;
    font-size: 40px;
    font-weight: 400;
    letter-spacing: 0.48em;
    padding-left: 0.48em;
    color: var(--ink);
  }
  .holder-name {
    position: absolute;
    left: 80px;
    top: 300px;
    margin: 0;
    font-size: 28px;
    font-weight: 500;
    line-height: 1.25;
    color: var(--ink);
  }
  .tagline {
    position: absolute;
    right: 80px;
    top: 250px;
    margin: 0;
    text-align: right;
    font-size: 21px;
    font-weight: 500;
    line-height: 1.25;
    color: var(--ink-soft);
  }
  .contact {
    position: absolute;
    right: 80px;
    bottom: 80px;
    margin: 0;
    text-align: right;
    font-size: 24px;
    font-weight: 500;
    line-height: 1.3;
    font-style: normal;
    color: var(--ink);
  }
</style>
</head>
<body>
  <main class="canvas">
    <section class="business-card">
      <div class="brand">
        <div class="brand-mark" aria-hidden="true"></div>
        <div class="brand-name">BRENQUORA</div>
      </div>
      <h1 class="holder-name">Mark<br>Tolley</h1>
      <p class="tagline">Lorem ipsum dolor<br>sit amet, consectetur</p>
      <address class="contact">
        580 812 73 46<br>
        info@brenquora.com
      </address>
    </section>
  </main>
</body>
</html>
```